Business Card Needed for Crafter of Pottery, Jewelry and Artwork

Calling all designers in search of an artistic challenge.

I need a new business card design for my pottery, jewelry and artwork business, Woven Glass and Tide, based in Vancouver BC.

I would like a card that is bright and inviting and preferably incorporates my logo and a sample of photos of my work while having a clean fresh look. The following contact details would preferably be included on the card as well:
• Melinda Osgood
• Designer
• Phone: 604.555.0147
• Email: Designer@WovenGlassandTide.example
• Website: www.WovenGlassandTide.example
• Blog: www.KilnNotesDaily.example

The logo is attached in two color schemes in both Vector and Source formats. On past cards I’ve also included photos of my work. By including photos of the work the pieces are showcased and it catches people’s eye and prompts them to pick up the card and look at it more closely. For example, if I leave a stack in a coffee shop I want people to be drawn to the card, to pick it up and get a sense of the my product lines. Please feel free to pull photos of my work directly off of my website. If you need photos with higher pixels please let me know and I’ll email them directly to you. The website background is bffbda (191, 251, 218). I would like the business cards to match the feel of the website for consistency but the cards do not need to use the exact same colors. My website and current business card are predominantly turquoise shades. The background uses stripes provided by the website template. I don’t know the exact colors of the stripes.

My current business card is attached to show the use of photos in a design. Please note that I am not thrilled with my own design and am looking for variations and completely new designs. This example is not meant to be used as a template or starting point.

Here is some background surrounding my company:
WGT offers one of a kind jewelry, pottery, artwork and leather bags each designed with a twist. The pottery varies from rustic every day functional ware to raku artwork. The jewelry ranges from simple sterling every day pieces to multimedia pieces incorporating stone, metal, ceramics and fabric. The artwork is multimedia, typically acrylic paired with a natural element such as bark. All the bags are leather with reworked kimono fabric or patterned silk lining.

Feel free to check out my website to get a flavour for my work and the color scheme I've used on marketing materials so far. www.wovenglassandtide.example
Updates

Thank you to everyone who has submitted a design so far. I hope everyone has received some helpful feedback.

I'm going to post a survey to customers and friends asking for their votes. If you have new designs to submit please try to get them in by Saturday March 30 at noon so that I can include it in the survey launch.

Thank you

Target Market(s)

Females aged 25-65 interested in one of a kind functional pottery and jewelry.

Industry/Entity Type

Coffee Shop

Requirements
Must have
• Contact information, website, blog
Nice to have
• Logo, photos

```html
<!DOCTYPE html>
<html lang="en">
<head>
<meta charset="utf-8">
<title>Woven Glass and Tide – Business Card</title>
<link href="https://fonts.googleapis.com/css2?family=EB+Garamond:wght@400;600&family=Italianno&display=swap" rel="stylesheet">
<style>
  :root {
    --navy: #07076a;
    --mint: #52e8b4;
    --mint-light: #7ff2c8;
    --royal: #2626d9;
    --white: #ffffff;
    --frame: #8a8a8a;
  }
  html, body { margin: 0; padding: 0; overflow: hidden; }
  body { width: 1200px; height: 900px; background: var(--white); position: relative; font-family: "EB Garamond", Georgia, serif; }
  .card { position: absolute; width: 702px; height: 400px; border: 1px solid var(--frame); box-sizing: border-box; overflow: hidden; background: var(--white); }
  .card--front { left: 62px; top: 48px; }
  .card--back { left: 376px; top: 476px; }
  .card svg.card__art { position: absolute; left: 0; top: 0; }
  .text { position: absolute; margin: 0; text-align: center; white-space: nowrap; transform: translateX(-50%); }
  .brand-name { left: 196px; top: 248px; font-size: 27px; font-weight: 600; color: var(--navy); letter-spacing: 1px; line-height: 1.1; white-space: normal; width: 230px; }
  .person-name { left: 505px; top: 48px; font-family: "Italianno", cursive; font-size: 62px; color: var(--royal); line-height: 1; }
  .person-role { left: 505px; top: 114px; font-size: 22px; color: var(--royal); }
  .phone { left: 505px; top: 242px; font-size: 38px; font-weight: 600; color: var(--mint); letter-spacing: 1px; }
  .email { left: 505px; top: 318px; font-size: 19px; color: var(--white); line-height: 26px; }
  .website { left: 351px; top: 282px; font-size: 38px; color: var(--white); letter-spacing: 1px; }
  .blog { left: 351px; top: 340px; font-size: 25px; color: var(--white); }
</style>
</head>
<body>
  <section class="card card--front">
    <svg class="card__art" width="702" height="400" viewBox="0 0 702 400">
      <rect class="contact-band" x="0" y="222" width="702" height="178" fill="var(--navy)"/>
      <circle class="logo-backdrop" cx="196" cy="198" r="166" fill="var(--white)"/>
      <circle class="logo-disc" cx="196" cy="198" r="150" fill="var(--mint)"/>
    </svg>
    <p class="text brand-name">Woven Glass and Tide</p>
    <p class="text person-name">Melinda Osgood</p>
    <p class="text person-role">Designer</p>
    <p class="text phone">604.555.0147</p>
    <p class="text email">Email:<br>Designer@WovenGlassandTide.example</p>
  </section>

  <section class="card card--back">
    <svg class="card__art" width="702" height="400" viewBox="0 0 702 400">
      <defs>
        <radialGradient id="bowlTone" cx="50%" cy="55%" r="60%">
          <stop offset="0" stop-color="#8fa6c9"/>
          <stop offset="0.55" stop-color="#3d4a5c"/>
          <stop offset="1" stop-color="#1c2330"/>
        </radialGradient>
        <linearGradient id="bustTone" x1="0" y1="0" x2="0" y2="1">
          <stop offset="0" stop-color="#e4dfcf"/>
          <stop offset="1" stop-color="#cfc8b4"/>
        </linearGradient>
      </defs>
      <path class="showcase-band" d="M0 196 H188 A152 74 0 0 0 492 196 H702 V400 H0 Z" fill="var(--navy)"/>
      <rect x="10" y="38" width="160" height="228" rx="6" fill="url(#bustTone)" role="img" aria-label="Photo: copper necklace with gemstone drops on a linen bust"/>
      <ellipse cx="336" cy="158" rx="152" ry="112" fill="url(#bowlTone)" role="img" aria-label="Photo: glazed blue-grey stoneware bowl seen from above"/>
      <rect x="534" y="36" width="160" height="230" rx="6" fill="url(#bustTone)" role="img" aria-label="Photo: turquoise bead necklace with stone pendant on a linen bust"/>
    </svg>
    <p class="text website">www.WovenGlassandTide.example</p>
    <p class="text blog">Blog: www.KilnNotesDaily.example</p>
  </section>
</body>
</html>
```